Wordpress Design Project (Brantvik)

We need a wordpress design for an established auction and real estate company based in Minnesota. The winning design will incorporate the colors of logo (red white and black) creatively in a very professional and clean layout. Client mentions liking the site http://www.dornwellsales.example/ and http://www.tarpliconauction.example/ as a general idea for what they like.

Industry/Entity Type

Real Estate

Requirements
Must have
• Navigation:
1) Home - will have auction list, no text
2) Upcoming Auctions
3) Online Auctions
4) Real Estate
5) Auction Gallery
6) For Sale
7) About Us
8) Contact Us

Sidebar widget will include:
- email signup
- asset for sale fader (seen in Featured Listings at http://www.tarpliconauction.example/)
- Slideshow - initial image attached
- Video widget (image attached)
- social media icons for Youtube, Facebook, Twitter, LinkedIn and RSS feed
- testimonials

Footer will have smaller logo and contact info
Nice to have
• Nice to Have:
- use of drop-down menu design for 'About Us'
1) About Brantvik
2) Testimonials

```html
<!DOCTYPE html>
<html lang="en">
<head>
<meta charset="utf-8">
<title>Brantvik Auction &amp; Real Estate Services</title>
<link href="https://fonts.googleapis.com/css2?family=Ubuntu:wght@400;500;700&family=Arimo:wght@400;700&display=swap" rel="stylesheet">
<style>
:root{
  --red:#b9262c;
  --red-dark:#9a1c21;
  --red-text:#a8232a;
  --tan:#c49a7c;
  --ink:#222;
  --grey:#555;
  --panel:#f2f2f2;
  --line:#d8d8d8;
}
*{box-sizing:border-box;margin:0;padding:0}
html,body{width:1067px;height:1200px;overflow:hidden;background:#fff}
body{position:relative;font-family:"Arimo",Arial,sans-serif;color:var(--ink)}
.abs{position:absolute}
.site-header{left:0;top:0;width:1067px;height:135px;background:linear-gradient(#fff,#f3f3f3)}
.brand{left:103px;top:24px;display:flex;align-items:center;gap:10px}
.brand-mark{width:34px;height:34px;background:var(--red)}
.brand-name{font-family:"Ubuntu",sans-serif;font-weight:700;font-size:44px;color:var(--red);letter-spacing:-1px}
.phone{left:822px;top:32px;font-family:"Ubuntu",sans-serif;font-size:22px;color:var(--red);display:flex;align-items:center;gap:10px}
.social{left:676px;top:86px;display:flex;align-items:center;gap:9px}
.social span{font-size:13px;margin-right:10px}
.social i{display:block;width:31px;height:31px;border-radius:6px}
.rule-top{left:0;top:135px;width:1067px;height:5px;background:var(--tan)}
.main-nav{left:0;top:142px;width:1067px;height:39px;background:linear-gradient(#c6343a,var(--red-dark));display:flex;align-items:center;padding-left:88px}
.main-nav a{font-family:"Ubuntu",sans-serif;font-size:12px;color:#fff;text-decoration:none;padding:0 26px;border-right:1px solid rgba(255,255,255,.35);line-height:22px}
.main-nav a:first-child{padding-left:16px}
.main-nav a:last-child{border:none}
.slider{left:97px;top:192px;width:635px;height:284px;background:#fff;box-shadow:0 8px 10px -6px rgba(0,0,0,.3);padding:5px}
.slide{width:625px;height:273px;background:linear-gradient(135deg,#3f8a3a,#8b8d7c 45%,#5f6b4a 70%,#2f7e34)}
.slider-bar{left:102px;top:443px;width:625px;height:27px;background:rgba(0,0,0,.55)}
.dot{top:451px;width:14px;height:14px;border-radius:50%;background:#fff}
.asset{left:739px;top:192px;width:237px;height:283px;border:1px solid var(--line);background:linear-gradient(#fff,#ececec);text-align:center}
.asset h3{font-weight:400;font-size:18px;padding:12px 0 8px;border-bottom:1px solid var(--line)}
.asset h3 em{font-style:normal;color:var(--red)}
.asset p{font-size:13px;color:var(--ink)}
.asset .thumb{width:175px;height:102px;margin:14px auto 26px;border:2px solid #111;background:linear-gradient(#cfd7dc,#e6e0d6 55%,#4d8a3c)}
.asset .link{color:var(--red-text);font-size:11px;line-height:16px}
.asset .addr{font-size:11px;line-height:16px}
.section-title{left:95px;top:509px;font-size:17px;letter-spacing:.2px;color:#222}
.card{left:92px;width:616px;border:1px solid var(--line);background:linear-gradient(#fff,#ececec)}
.card-head,.side-head{height:34px;background:linear-gradient(#c6343a,var(--red-dark));color:#fff;font-weight:700;font-size:14px;letter-spacing:.3px;line-height:34px;padding-left:10px}
.card .photo{position:absolute;left:12px;top:61px;width:132px;height:92px;border:1px solid #3b6ab0;background:linear-gradient(#c5d1dc,#d9d5cc 55%,#5a8a45)}
.details-btn{position:absolute;left:11px;top:168px;width:134px;height:33px;border-radius:6px;background:linear-gradient(#4a4a4a,#111);color:#fff;font-weight:700;font-size:15px;display:flex;align-items:center;gap:10px;padding-left:12px;letter-spacing:.5px}
.card .info{position:absolute;left:162px;top:60px;width:445px;font-size:12.5px;line-height:14.5px}
.card .info h4{color:var(--red-text);font-size:13px;letter-spacing:.3px;line-height:16px;margin-bottom:10px}
.card .when{position:absolute;left:164px;top:176px;font-size:12.5px;line-height:17.5px}
.card .when b{color:var(--red-text);font-size:11.5px}
.video{left:739px;top:545px;width:237px;height:221px;border:1px solid var(--line);background:#fff}
.side-head{font-weight:400;font-family:"Ubuntu",sans-serif;font-size:16px;padding-left:11px}
.video-frame{margin:8px 3px 0;height:176px;background:linear-gradient(#7d7d7d,#c7c7c7 40%,#8a1f22 55%,#d8d8d8 80%,#111 92%);position:relative}
.video-frame span{position:absolute;left:10px;top:8px;color:#fff;font-size:11px;font-weight:700}
.testimonials{left:739px;top:810px;width:238px;height:245px;border:1px solid var(--line);background:linear-gradient(#fff,#ececec)}
.quote{width:212px;padding:12px 0 0 0;margin-left:20px;font-size:11px;line-height:15px;color:#333;position:relative}
.quote p{width:190px}
.quote::before{content:"\201C";position:absolute;left:-12px;top:5px;font-size:18px;font-weight:700}
.quote .close{position:absolute;right:4px;top:46px;font-size:18px;font-weight:700;line-height:10px}
.quote cite{display:block;text-align:right;font-style:normal;font-weight:700;color:var(--red-text);margin-top:10px;padding-right:4px}
.quote+.quote{border-top:1px solid var(--line);margin:12px 8px 0 8px;width:221px;padding:14px 0 0 17px}
.quote+.quote::before{left:5px;top:13px}
.quote+.quote .close{top:48px}
.rule-foot{left:0;top:1071px;width:1067px;height:6px;background:var(--tan)}
.footer-info{left:95px;top:1090px;font-family:"Ubuntu",sans-serif;font-weight:700;font-size:12px;line-height:16px}
.copyright{left:93px;top:1164px;font-size:11.5px}
.footer-brand{left:850px;top:1103px;display:flex;align-items:center;gap:7px}
.footer-brand .brand-mark{width:18px;height:18px}
.footer-brand .brand-name{font-size:26px}
.footer-band{left:0;top:1191px;width:1067px;height:9px;background:var(--red)}
</style>
</head>
<body>
<header class="site-header abs">
  <div class="brand abs"><i class="brand-mark"></i><span class="brand-name">Brantvik</span></div>
  <div class="phone abs">
    <svg width="12" height="24" viewBox="0 0 12 24"><path d="M9 1H4C2 1 1 3 1 5v14c0 2 1 4 3 4h5v-5H6V6h3z" fill="#b9262c"/></svg>
    555 014 2290
  </div>
  <div class="social abs">
    <span>Stay Connected</span>
    <i style="background:#c9302c" aria-label="Video channel"></i>
    <i style="background:#3b5a98" aria-label="Community page"></i>
    <i style="background:#3c5d74" aria-label="Short updates"></i>
    <i style="background:#1a86c8" aria-label="Business profile"></i>
    <i style="background:#f08a1c" aria-label="News feed"></i>
  </div>
</header>
<div class="rule-top abs"></div>
<nav class="main-nav abs">
  <a href="#">Home</a><a href="#">Upcoming Auctions</a><a href="#">Online Auctions</a><a href="#">Real Estate</a><a href="#">Auction Gallery</a><a href="#">For Sale</a><a href="#">About US</a><a href="#">Contact Us</a>
</nav>

<div class="slider abs"><div class="slide" role="img" aria-label="Crowd at an outdoor farm equipment auction"></div></div>
<div class="slider-bar abs"></div>
<i class="dot abs" style="left:633px;background:var(--red)"></i>
<i class="dot abs" style="left:655px"></i>
<i class="dot abs" style="left:678px"></i>

<aside class="asset abs">
  <h3><em>Asset</em> for sale</h3>
  <p style="margin-top:12px">Lots 30 &amp; 49 for sale, Millbrook Iowa</p>
  <div class="thumb" role="img" aria-label="Modern two-storey house on a lawn"></div>
  <p class="link">Fair Oaks home w/1.25 acres</p>
  <p class="addr">1820 S Alder, Fair Oaks, IA 52699</p>
</aside>

<h2 class="section-title abs" style="font-weight:400">CURRENT &amp; UPCOMING AUCTIONS</h2>

<article class="card abs" style="top:545px;height:239px">
  <div class="card-head">CEDARLINE PHYSICAL THERAPY IN ASHFORD, GA</div>
  <div class="photo" role="img" aria-label="Large family house with landscaped garden"></div>
  <div class="info"><h4>Hollis Marsh Auctions, LLC GAL 4812 - Everything sold to the high<br>bidder</h4>
    Location:<br>Location 1 - 410 Ridgeview Hwy<br>Location 2 - 52 Creek Mdws # 2<br>Ashford, GA 30599</div>
  <div class="details-btn"><svg width="22" height="22" viewBox="0 0 22 22"><circle cx="9" cy="9" r="6.5" fill="none" stroke="#fff" stroke-width="2.2"/><path d="M14 14l6 6" stroke="#fff" stroke-width="3"/></svg>DETAILS</div>
  <div class="when"><b>Online Bidding Only</b><br>Began:&nbsp; Friday, May 24, 2013 at 10:06 AM EDT<br>Ends:&nbsp; Wednesday, June 05, 2013 at 10:00 AM EDT</div>
</article>

<article class="card abs" style="top:810px;height:245px">
  <div class="card-head" style="padding-left:15px">CEDARLINE PHYSICAL THERAPY IN ASHFORD, GA</div>
  <div class="photo" style="left:17px" role="img" aria-label="Large family house with landscaped garden"></div>
  <div class="info" style="left:168px"><h4>Hollis Marsh Auctions, LLC GAL 4812 - Everything sold to the high<br>bidder</h4>
    Location:<br>Location 1 - 410 Ridgeview Hwy<br>Location 2 - 52 Creek Mdws # 2<br>Ashford, GA 30599</div>
  <div class="details-btn" style="left:17px"><svg width="22" height="22" viewBox="0 0 22 22"><circle cx="9" cy="9" r="6.5" fill="none" stroke="#fff" stroke-width="2.2"/><path d="M14 14l6 6" stroke="#fff" stroke-width="3"/></svg>DETAILS</div>
  <div class="when" style="left:170px"><b>Online Bidding Only</b><br>Began:&nbsp; Friday, May 24, 2013 at 10:06 AM EDT<br>Ends:&nbsp; Wednesday, June 05, 2013 at 10:00 AM EDT</div>
</article>

<aside class="video abs">
  <div class="side-head">WATCH VIDEO</div>
  <div class="video-frame" role="img" aria-label="Bidder tutorial video showing the online bidding screen">
    <span>Brantvik Bidder Tutorial.mp4</span>
    <svg style="position:absolute;left:103px;top:76px" width="34" height="34" viewBox="0 0 34 34"><circle cx="17" cy="17" r="15" fill="rgba(255,255,255,.35)" stroke="#fff" stroke-width="2"/><path d="M13 10l11 7-11 7z" fill="#fff"/></svg>
  </div>
</aside>

<aside class="testimonials abs">
  <div class="side-head" style="padding-left:19px">CLIENT TESTIMONIALS</div>
  <blockquote class="quote"><p>Lorem Ipsum is simply dummy text of<br>the printing and typesetting industry.<br>Lorem Ipsum Lorem Ipsum&nbsp; Lorem</p><span class="close">&rdquo;</span><cite>Mr Alden Pryce</cite></blockquote>
  <blockquote class="quote"><p>Lorem Ipsum is simply dummy text of<br>the printing and typesetting industry.<br>Lorem Ipsum Lorem Ipsum&nbsp; Lorem</p><span class="close">&rdquo;</span><cite>Mr Alden Pryce</cite></blockquote>
</aside>

<div class="rule-foot abs"></div>
<footer>
  <address class="footer-info abs" style="font-style:normal">Brantvik&nbsp; Auctioneers<br>118 4th Street NW • Lakeview, FL 33899<br>P: 555-014-7867 • F: 555-014-7879<br>Email : info@brantvik.example</address>
  <p class="copyright abs">Copyright (C) Brantvik 2013 - 2014 .&nbsp; All Rights Reserved</p>
  <div class="footer-brand abs"><i class="brand-mark"></i><span class="brand-name">Brantvik</span></div>
  <div class="footer-band abs"></div>
</footer>
</body>
</html>
```